Cedar Steam & Sauna Digital Billboard

This is a digital billboard so we are looking for a fresh design that will capture people's attention. The current billboard is a simple black text "#FeelTheWarmth" over a white background with a picture of an iphone with one of our photos (Reference attached) We enjoy how clean and simple this design is, but open to other concepts. Since the weather is getting colder, a lot of people come to our spa because we offer various dry saunas and hot baths in addition to our spa services. We have a few photos for reference on our website information view www.cedarsteamhouse.com , but you can email me for additional photo content - moreno@cedarsteamhouse.com

Target Market(s)

New Jersey Locals

Colors
0255a3
ec1f27
f37122
ffc214

Requirements
Must have
• Font is "Barlow"
Nice to have
• #FeelTheWarmth hashtag

```html
<!DOCTYPE html>
<html lang="en">
<head>
<meta charset="utf-8">
<title>Cedar Steam &amp; Sauna – Digital Billboard</title>
<link rel="stylesheet" href="https://fonts.googleapis.com/css2?family=Barlow:wght@300;400;500&display=swap">
<style>
  :root {
    --paper: #ffffff;
    --ink: #111111;
    --frame: #1a1a1a;
    --brand-blue: #0255a3;
    --brand-red: #ec1f27;
    --brand-orange: #f37122;
    --brand-yellow: #ffc214;
    --warm-light: #f6e3bf;
    --warm-deep: #6b3418;
  }
  * { margin: 0; padding: 0; box-sizing: border-box; }
  html, body {
    width: 1200px;
    height: 454px;
    overflow: hidden;
    background: var(--paper);
  }
  .billboard {
    position: relative;
    width: 1200px;
    height: 454px;
    background: var(--paper);
    font-family: "Barlow", sans-serif;
    color: var(--ink);
  }
  .billboard__photo {
    position: absolute;
    left: 0;
    top: 0;
    width: 760px;
    height: 454px;
  }
  .billboard__frame {
    position: absolute;
    left: 37px;
    top: 48px;
    width: 1126px;
    height: 360px;
    border: 2px solid var(--frame);
    pointer-events: none;
  }
  .billboard__message {
    position: absolute;
    left: 730px;
    top: 0;
    width: 400px;
    height: 454px;
    text-align: center;
  }
  .hashtag {
    position: absolute;
    left: 0;
    top: 104px;
    width: 400px;
    font-size: 54px;
    font-weight: 300;
    line-height: 1;
    white-space: nowrap;
  }
  .brand {
    position: absolute;
    left: 0;
    top: 252px;
    width: 400px;
    display: flex;
    flex-direction: column;
    align-items: center;
  }
  .brand__dot {
    width: 30px;
    height: 30px;
    border-radius: 50%;
    background: var(--brand-yellow);
  }
  .brand__name {
    margin-top: 12px;
    font-size: 21px;
    font-weight: 500;
    letter-spacing: 1.5px;
    line-height: 1.2;
    color: var(--brand-blue);
  }
  .brand__url {
    margin-top: 10px;
    font-size: 18px;
    font-weight: 400;
    line-height: 1.2;
  }
</style>
</head>
<body>
  <main class="billboard">
    <svg class="billboard__photo" viewBox="0 0 760 454" role="img"
         aria-label="Warm-lit spa interior with wooden sauna cabins and a guest resting inside a glowing sauna room, shown in a brush-stroke shape">
      <defs>
        <linearGradient id="spa-tones" x1="0" y1="0" x2="1" y2="0.3">
          <stop offset="0" stop-color="var(--warm-light)"/>
          <stop offset="0.4" stop-color="var(--brand-yellow)" stop-opacity="0.85"/>
          <stop offset="0.7" stop-color="var(--brand-orange)"/>
          <stop offset="1" stop-color="var(--warm-deep)"/>
        </linearGradient>
      </defs>
      <path fill="url(#spa-tones)" d="
        M0 90 L60 70 L150 40 L230 20 L330 12 L420 0 L540 0 L620 20 L650 60
        L700 70 L680 100 L720 130 L700 170 L740 200 L710 240 L716 260
        L690 300 L640 330 L560 360 L480 380 L420 410 L360 440 L320 454
        L0 454 Z"/>
    </svg>

    <div class="billboard__frame"></div>

    <section class="billboard__message">
      <h1 class="hashtag">#FeelTheWarmth</h1>
      <div class="brand">
        <span class="brand__dot"></span>
        <p class="brand__name">Cedar Steam &amp; Sauna</p>
        <p class="brand__url">www.cedarsteamhouse.com</p>
      </div>
    </section>
  </main>
</body>
</html>
```